依頼概要
■依頼の目的/概要
弊社の経営理念を作成しましたが、社内掲示用にポスターの作成をお願いします。

■依頼詳細
ミッション・ビジョン・バリューをポスター1枚に収めてください。
HPにも掲載できればと考えています。

■重視する点
掲載内容は添付ファイルをご確認ください。

過去の提案(同業者なので)を見て応募しようと考えました。
https://www.pitchora.jp/work/detail/4731852

■弊社の紹介
東京都内で廃棄物を収集・処分する会社です。詳しくは下記Official HPをご覧ください。
https://www.miyakura-k.co.jp

HP検討挿入予定個所
https://www.miyakura-k.co.jp/company

■その他
掲載内容の文言はあまり整理されていないのでうまい具合にご調整ください。

■その他ご不明点はお気軽にお問合せください。

発注時のイメージ通りの作品だったため。

この度は、沢山のご応募ありがとうございます。
皆さんのご提案が多く、選定に迷いました。

また機会がございましたら、よろしくお願いします。

```html
<!DOCTYPE html>
<html lang="ja">
<head>
<meta charset="utf-8">
<title>MIYAKURA 経営理念</title>
<link rel="stylesheet" href="https://fonts.googleapis.com/css2?family=Montserrat:wght@700;800&family=Noto+Sans+JP:wght@500;700;900&display=swap">
<style>
  :root {
    --navy: #1d3a78;
    --navy-deep: #152c5e;
    --accent: #3fb6e8;
    --body-text: #ffffff;
    --rule: #1d3a78;
    --forest-light: #dfe9d4;
    --forest-mid: #9fbf8c;
    --forest-deep: #55804a;
    --text-halo: rgba(28, 52, 32, 0.75);
  }
  * { margin: 0; padding: 0; box-sizing: border-box; }
  html, body { width: 852px; height: 1200px; overflow: hidden; background: #ffffff; }
  .poster {
    position: relative;
    width: 852px;
    height: 1200px;
    overflow: hidden;
    font-family: "Noto Sans JP", sans-serif;
  }
  .forest-backdrop {
    position: absolute;
    inset: 0;
    background:
      radial-gradient(ellipse 45% 30% at 50% 20%, rgba(255,255,255,0.7), rgba(255,255,255,0) 70%),
      radial-gradient(ellipse 40% 60% at 8% 65%, rgba(85,128,74,0.6), rgba(85,128,74,0) 70%),
      radial-gradient(ellipse 40% 60% at 94% 55%, rgba(85,128,74,0.55), rgba(85,128,74,0) 70%),
      linear-gradient(180deg, var(--forest-mid) 0%, var(--forest-light) 18%, #c6d9b6 45%, var(--forest-mid) 75%, var(--forest-deep) 100%);
  }
  .brand {
    position: absolute;
    left: 58px;
    top: 56px;
    display: flex;
    align-items: center;
    gap: 12px;
  }
  .brand-mark {
    width: 34px;
    height: 34px;
    border-radius: 50%;
    background: var(--accent);
  }
  .brand-name {
    font-weight: 900;
    font-size: 30px;
    letter-spacing: 1px;
    color: var(--navy);
    line-height: 1;
  }
  .brand-sub {
    display: block;
    margin-top: 5px;
    font-size: 11px;
    font-weight: 500;
    letter-spacing: 2px;
    color: var(--navy);
  }
  .principle {
    position: absolute;
    left: 105px;
    width: 680px;
  }
  .principle-head {
    display: flex;
    align-items: center;
    border-bottom: 3px solid var(--rule);
  }
  .principle-label {
    width: 178px;
    height: 46px;
    background: var(--navy);
    color: #ffffff;
    font-family: "Montserrat", sans-serif;
    font-weight: 800;
    font-size: 30px;
    letter-spacing: 1px;
    display: flex;
    align-items: center;
    justify-content: center;
  }
  .principle-label .initial { color: var(--accent); }
  .principle-title {
    margin-left: 22px;
    font-weight: 900;
    font-size: 30px;
    color: var(--navy-deep);
    letter-spacing: 2px;
  }
  .principle-body {
    margin-top: 14px;
    font-weight: 700;
    font-size: 27px;
    line-height: 46px;
    letter-spacing: 1.5px;
    color: var(--body-text);
    white-space: nowrap;
    text-shadow: 0 0 6px var(--text-halo), 0 1px 2px rgba(0, 0, 0, 0.45);
  }
  .principle--mission { top: 226px; }
  .principle--vision { top: 500px; }
  .principle--value { top: 790px; }
</style>
</head>
<body>
<main class="poster">
  <div class="forest-backdrop" role="img" aria-label="木漏れ日が差し込む明るい緑の森の写真"></div>

  <header class="brand">
    <span class="brand-mark"></span>
    <div>
      <span class="brand-name">MIYAKURA</span>
      <span class="brand-sub">株式会社ミヤクラ</span>
    </div>
  </header>

  <section class="principle principle--mission">
    <div class="principle-head">
      <div class="principle-label"><span class="initial">M</span>ission</div>
      <h2 class="principle-title">社会的使命</h2>
    </div>
    <p class="principle-body">
      地球環境を保全するために、静脈産業を支える<br>
      社会インフラの一部としての役割を全うし、<br>
      すべての人に快適でクリーンな世界を提供する
    </p>
  </section>

  <section class="principle principle--vision">
    <div class="principle-head">
      <div class="principle-label"><span class="initial">V</span>ision</div>
      <h2 class="principle-title">中長期計画</h2>
    </div>
    <p class="principle-body">
      先進的(Advanced)な取り組みを行い<br>
      廃棄物業界リード(Lead)し<br>
      高品質(High quality)なサービスを提供し<br>
      働きがいのある(Satisfaction)会社づくりを行う
    </p>
  </section>

  <section class="principle principle--value">
    <div class="principle-head">
      <div class="principle-label"><span class="initial">V</span>alue</div>
      <h2 class="principle-title">大切な価値観</h2>
    </div>
    <p class="principle-body">
      活発なコミュニケーションの元、情報共有を行い、<br>
      チームワーク溢れる組織風土の中で、共働し、<br>
      何事にも真摯に向き合い、正直な気持ちで、<br>
      チャレンジ行動力をもって、自己実現を目指す
    </p>
  </section>
</main>
</body>
</html>
```